DEIJ Annual Progress Report

We need a Word-based year-end progress report for The Calloway Partners, Inc. for their client Brookvale Care Network. The report should be easily editable because this report represents the first draft. We want the report to use The Calloway Partners, Inc.'s colors as the main color and incorporate the client's colors as ascents. Please provide two spots per page where photos can be inserted.
Updates

Please include an introduction and conclusion paragraph. I will add that text later.

I uploaded the introduction and conclusion to use with the report.

Give some designer a chance to response, or update their designs.

Target Market(s)

Healthcare Executives

Industry/Entity Type

Healthcare consulting

Font styles to use
Other font styles liked:
• Loto, and Raleway

Requirements
Must have
• Use of the TCP and BVCN logos, appropriate photos in case I go with stock photos
Nice to have
• Warm but professional feeling
Should not have
• Cartoons, silly or funny pictures

```html
<!DOCTYPE html>
<html lang="en">
<head>
<meta charset="utf-8">
<title>The Calloway Partners – DEIJ Progress Report</title>
<link href="https://fonts.googleapis.com/css2?family=Montserrat:wght@600;700;800&family=Lato:ital,wght@0,400;0,700;1,400&display=swap" rel="stylesheet">
<style>
:root{
  --navy:#2c2a7c;
  --navy-deep:#221f63;
  --gold:#b98f3f;
  --cream:#f2eee3;
  --paper:#f7f4ec;
  --ink:#2a2a3a;
  --stage:#e6e6e8;
  --blue-soft:#6f8fc7;
}
*{box-sizing:border-box;margin:0;padding:0}
html,body{width:720px;height:1200px;overflow:hidden;background:var(--stage)}
body{position:relative;font-family:'Lato',sans-serif;color:var(--ink)}
.page{position:absolute;background:var(--paper);overflow:hidden;box-shadow:0 2px 8px rgba(0,0,0,.12)}

/* front cover */
.front-cover{left:370px;top:80px;width:330px;height:467px;background:var(--cream)}
.brand{position:absolute;display:flex;align-items:center;gap:8px}
.brand-dot{width:34px;height:34px;border-radius:50%;border:4px solid var(--navy);flex:none}
.brand-name{font-family:'Montserrat',sans-serif;font-weight:800;font-size:15px;line-height:1.05;color:var(--navy);text-transform:uppercase}
.brand-tagline{position:absolute;font-size:7px;font-style:italic;color:var(--navy);line-height:1.3}
.front-cover .brand{left:70px;top:32px}
.front-cover .brand-tagline{left:116px;top:78px}
.cover-rule{position:absolute;right:0;top:100px;width:190px;height:6px;background:var(--navy)}
.cover-photo{position:absolute;left:0;right:0;top:106px;height:196px;background:linear-gradient(180deg,#4a4a52 0%,#9d8f7e 45%,#6b5e52 100%)}
.cover-gold{position:absolute;left:0;top:302px;width:190px;height:5px;background:var(--gold)}
.cover-headline{position:absolute;left:0;right:0;top:340px;text-align:center;font-family:'Montserrat',sans-serif;font-weight:700;font-size:12.5px;color:var(--navy);letter-spacing:.2px}
.cover-sub{position:absolute;left:20px;right:20px;top:362px;text-align:center;font-size:9.5px;color:var(--gold);line-height:1.35}
.cover-web{position:absolute;left:0;right:0;top:410px;text-align:center;font-size:8.5px;font-weight:700;letter-spacing:.8px;color:var(--navy)}

/* back cover */
.back-cover{left:20px;top:80px;width:330px;height:467px;background:linear-gradient(180deg,#1c1b2a 0%,#2e3f66 38%,var(--navy) 62%,var(--navy-deep) 100%)}
.back-photo{position:absolute;left:0;right:0;top:0;height:250px;background:linear-gradient(160deg,#2a2a35 0%,#5e7fa8 55%,rgba(44,42,124,0) 100%)}
.back-cover .brand{left:96px;top:292px}
.back-cover .brand-dot{border-color:#fff}
.back-cover .brand-name{color:#fff}
.contact{position:absolute;left:96px;top:348px;list-style:none}
.contact li{font-size:11px;color:#fff;margin-bottom:8px}
.contact span{font-size:7.5px;color:var(--gold);margin-right:4px}
.back-gold{position:absolute;left:0;right:0;bottom:0;height:4px;background:var(--gold)}

/* spread */
.spread-page{top:590px;width:340px;height:481px}
.left-page{left:20px}
.right-page{left:360px;box-shadow:0 2px 8px rgba(0,0,0,.12),inset 8px 0 10px -8px rgba(0,0,0,.2)}
.team-photo{position:absolute;left:56px;top:18px;width:270px;height:112px;background:linear-gradient(120deg,#c9d3de,#8a8b92 50%,#3f4a6a)}
.headshot{position:absolute;left:206px;top:96px;width:66px;height:66px;background:linear-gradient(160deg,#d8d0c2,#6b5a4c)}
.section-ribbon{position:absolute;left:0;top:150px;width:170px;height:18px;background:var(--navy);color:var(--gold);font-family:'Montserrat',sans-serif;font-weight:700;font-size:9px;letter-spacing:.6px;padding:3px 0 0 22px}
.body-col{position:absolute;font-size:5.8px;line-height:1.4;text-align:justify;color:var(--ink)}
.body-col p{margin-bottom:4px}
.left-col-a{left:22px;top:178px;width:142px}
.left-col-b{left:176px;top:178px;width:146px}
.motif-panel{position:absolute;left:40px;top:428px;width:124px;height:32px;border-radius:3px;background:linear-gradient(100deg,rgba(185,143,63,.18),rgba(111,143,199,.22) 55%,rgba(44,42,124,.16))}
.page-foot{position:absolute;left:0;right:0;bottom:10px;height:4px;display:flex}
.page-foot .n{flex:3;background:var(--navy)}
.page-foot .g{flex:1;background:var(--gold)}

.puzzle-photo{position:absolute;left:120px;top:18px;width:206px;height:98px;border:1px solid var(--gold);background:linear-gradient(120deg,#eef0f3,#d9c3ad 50%,#b78f78)}
.report-title{position:absolute;left:20px;top:104px;width:160px;padding:8px 10px;background:var(--navy);color:#fff;font-family:'Montserrat',sans-serif;font-weight:600;font-size:8.3px;line-height:1.3}
.progress-head{position:absolute;left:22px;top:176px;font-family:'Montserrat',sans-serif;font-weight:800;font-size:10px;color:var(--navy);display:flex;align-items:center;gap:5px}
.progress-head i{width:8px;height:8px;border-radius:50%;border:2px solid var(--navy)}
.bullets{position:absolute;font-size:5.6px;line-height:1.38;color:var(--ink);list-style:none}
.bullets>li{margin-bottom:4px}
.bullets h4{font-size:6px;color:var(--gold);font-weight:700}
.bullets h4::before{content:"• ";color:var(--gold)}
.bullets ul{list-style:none;padding-left:7px}
.bullets ul li::before{content:"o ";}
.bullets-a{left:22px;top:194px;width:150px}
.bullets-b{left:184px;top:150px;width:138px}
</style>
</head>
<body>

<section class="page back-cover">
  <div class="back-photo" role="img" aria-label="Photo of a hand touching a glowing digital network interface"></div>
  <div class="brand"><span class="brand-dot"></span><span class="brand-name">The Calloway<br>Partners Inc.</span></div>
  <ul class="contact">
    <li><span>Mobile:</span>+1 555-014-0199</li>
    <li><span>Email:</span>contact@callowaypartners.com</li>
    <li><span>Websites:</span>www.callowaypartners.com</li>
  </ul>
  <div class="back-gold"></div>
</section>

<section class="page front-cover">
  <div class="brand"><span class="brand-dot"></span><span class="brand-name">The Calloway<br>Partners Inc.</span></div>
  <p class="brand-tagline">Transformative, Sustainable Solutions<br>for Equity and Inclusion</p>
  <div class="cover-rule"></div>
  <div class="cover-photo" role="img" aria-label="Photo of classical stone columns and wide steps of a courthouse"></div>
  <div class="cover-gold"></div>
  <h1 class="cover-headline">COURAGEOUSLY CENTER EQUITY AND JUSTICE</h1>
  <p class="cover-sub">Unleash a dynamic culture that celebrates your diverse strengths, unlocks hidden talents, and centers justice.</p>
  <p class="cover-web">www.callowaypartners.com</p>
</section>

<section class="page spread-page left-page">
  <div class="team-photo" role="img" aria-label="Photo of a diverse team meeting around laptops"></div>
  <div class="headshot" role="img" aria-label="Portrait photo placeholder"></div>
  <h2 class="section-ribbon">INTRODUCTION</h2>
  <div class="body-col left-col-a">
    <p>The Calloway Partners, Inc., a Black woman-owned global diversity, equity, inclusion, and justice (DEIJ) consulting firm established in 1984, brings over 80 years of combined experience in its field. Specializing in learning and education, cultural audits, and strategy development, the firm is dedicated to centering its work on those most impacted by injustice and oppression. Through advancing DEIJ thought leadership and partnering with committed organizations, The Calloway Partners strives to build equitable and just systems within workplaces and beyond.</p>
    <p>Our collaboration with Brookvale Care Network (BVCN), focused on providing Backbone Support for their Anti-Racism Road Map, has been a source of both honor and pleasure. This partnership aims to enhance BVCN's capacity to deliver exceptional patient care in diverse communities, fostering an anti-racist and equitable healthcare environment that actively confronts all forms of racism while promoting greater diversity, inclusion, and equity among its workforce and those it serves.</p>
    <p>This report outlines The Calloway Partners, Inc.'s role, achievements, and contributions to BVCN in 2023 and presents forward-looking recommendations to further advance the Equity and Anti-Racism Roadmap.</p>
  </div>
  <div class="body-col left-col-b">
    <p>Throughout 2023, The Calloway Partners, Inc. has achieved significant milestones in collaboration with Brookvale Care Network (BVCN). Notably, we successfully facilitated the development and implementation of comprehensive DEIJ strategies, which included the integration of a learning journey within the leadership model and the effective alignment of various strategic initiatives under the Anti-Racism Road Map. Our efforts in conducting cultural audits and enhancing operational efficiencies have been instrumental in advancing BVCN's commitment to equity and inclusion.</p>
    <p>Looking ahead, this report will unveil insightful recommendations that build upon these accomplishments. We propose strategic initiatives that not only consolidate our past successes but also chart a path forward for sustained impact. These recommendations are designed to deepen BVCN's commitment to anti-racism, broaden its scope to embrace intersectionality, and further integrate patient and community voices into its framework. We believe that the implementation of these recommendations will be pivotal in elevating BVCN's position as a leader in equitable healthcare delivery. We invite you to explore the detailed insights and strategic directions outlined in the subsequent sections of this report.</p>
  </div>
  <div class="motif-panel" role="img" aria-label="Decorative word arrangement in navy, gold and blue"></div>
  <div class="page-foot"><span class="n"></span><span class="g"></span></div>
</section>

<section class="page spread-page right-page">
  <div class="puzzle-photo" role="img" aria-label="Photo of two hands joining puzzle pieces"></div>
  <h2 class="report-title">The Calloway Partners, Inc. Backbone Support 2023 Progress Report Driving Anti-Racism Strategy at Brookvale Care Network</h2>
  <h3 class="progress-head">PROGRESS <i></i></h3>
  <ul class="bullets bullets-a">
    <li><h4>Guiding Vision and Strategy</h4>
      <ul>
        <li>Facilitated the development of four synergistic goals derived from 11 strategies.</li>
        <li>Spearheaded EDLB, PI, and Strategy Lead presentations to track progress and set objectives.</li>
        <li>Played a pivotal role in shaping goals and defining measures of success.</li>
        <li>Picture: EDLB presentations and Strategy Leads' testimonials confirm the guidance.</li>
      </ul></li>
    <li><h4>Supporting Aligned Activities</h4>
      <ul>
        <li>Coaches worked closely with strategy leads to define actions for strategy advancement.</li>
        <li>Developed a coaching template integrating a learning journey within the BVCN leadership model.</li>
        <li>Ensured alignment and synergy among Strategies Leads to further collective goals.</li>
        <li>Picture: documentation of the learning journey's integration with the leadership model.</li>
      </ul></li>
    <li><h4>Establishing Shared Measurement Practices</h4>
      <ul>
        <li>Led the creation of four overarching goals aligning with 11 strategies.</li>
        <li>Initiated the development of success objectives and their transformation into measurable indicators.</li>
        <li>Took charge of establishing shared goals and the methodology for measuring success.</li>
        <li>Picture: The actual goals and objectives documents that illustrate the use of shared data in decision-making processes.</li>
      </ul></li>
  </ul>
  <ul class="bullets bullets-b">
    <li><h4>Building Public Will</h4>
      <ul>
        <li>Proposed and participated in the D&amp;I Summit, with our CEO as a key speaker.</li>
        <li>Actively participated in executive diversity leadership boards (EDLB) meetings.</li>
        <li>Participated in internal and potential external support through annual reports and publications.</li>
        <li>Picture: Event agendas and recordings, feedback surveys from the D&amp;I Summit, communication materials such as newsletters or annual reports, and media coverage of public engagements.</li>
      </ul></li>
    <li><h4>Fostering Continuous Learning and Development</h4>
      <ul>
        <li>Integrated coaching with the existing leadership model, adding depth with a focus on anti-racist leadership.</li>
        <li>Embedded wellness and resilience-building within strategic development.</li>
        <li>The Calloway Partners, Inc. CEO was actively involved in providing continuous learning.</li>
        <li>Picture: Descriptions of the leadership model enhancements, training materials, participant feedback on learning and development programs, and case studies of how the learning has been applied.</li>
      </ul></li>
  </ul>
  <div class="page-foot"><span class="n"></span><span class="g"></span></div>
</section>

</body>
</html>
```